LABEL DESIGNS FOR SKINCARE LINE

Hello we are needing 12 label various label designs but would like to see you design ONE. We will pick winner from this and send the rest.
LABEL SIZE -2x7
JAR SIZE IS - 8oz
LOGOS FILES BELOW
https://vault.parcelnook.net/share/folders/7Kp3wQ-zrTbnvLoYcDFeMJHAXUw9PsR2a
INFORMATION FOR LABEL
Lumi Dawn Halo Whipped Body Sugar Scrub 8oz
Ideal for all Skin Types
Ingredients:
Pure Cane Sugar, Extra Virgin Coconut Oil, Mango Butter, Kukum Butter, Emulsifying Wax, Jojoba Seed Oil, Sweet Almond Oil, Strawberry Essential Oil, and Pomegranate Essential Oil.
Directions to use Body Sugar Scrub:
Apply to wet skin gently in a circular motion on desired body area, hands, feet, legs, arms, etc. Once you have a good scrub, rinse, pat dry, and enjoy soft, hydrated skin. Best to use in the shower. Use between 2-3 times a week if needed.
*Cautions:
(1) Allergy: Approach this product with extreme caution, if you have allergies
(2) Avoid direct contact with eyes
Storage/Shelf Life of Product:
For best results, stir/mix scrub with the wooden or plastic spoon before each use. The shelf life of all sugar scrubs is 6-8 weeks. Keep the product in a cool, dry place, away from hot or heated temperatures.
All Natural, Cruelty-Free, Vegan Free
No Mineral Oil
No Petroleum
No Parabens

```html
<!DOCTYPE html>
<html lang="en">
<head>
<meta charset="utf-8">
<title>Lumi Dawn Halo – Whipped Body Sugar Scrub Label</title>
<link href="https://fonts.googleapis.com/css2?family=Courgette&family=Lato:wght@400;700&family=Roboto:wght@500&display=swap" rel="stylesheet">
<style>
  :root{
    --backdrop:#cfd0d2;
    --label-pink:#f49aab;
    --lid-pink:#e9889a;
    --berry:#b0236b;
    --ink:#241a1e;
    --band:#e9e9eb;
    --white:#ffffff;
  }
  html,body{margin:0;padding:0;overflow:hidden;}
  body{width:1200px;height:900px;background:var(--backdrop);position:relative;font-family:"Lato",sans-serif;color:var(--ink);}
  .lid-label{position:absolute;left:400px;top:50px;width:400px;height:400px;}
  .lid-label .arc-text{font-family:"Roboto",sans-serif;font-weight:500;font-size:25px;letter-spacing:4px;fill:var(--berry);}
  .lid-label .brand{font-family:"Lato",sans-serif;font-weight:700;font-size:22px;fill:var(--white);}
  .lid-label .title{font-family:"Courgette",cursive;font-size:44px;fill:var(--berry);}

  .wrap-label{position:absolute;left:50px;top:530px;width:1100px;height:314px;box-shadow:0 2px 6px rgba(0,0,0,.18);overflow:hidden;}
  .wrap-label .field{position:absolute;inset:0;}
  .info{position:absolute;top:29px;width:281px;font-size:12.2px;line-height:14.2px;text-align:justify;}
  .info h3{margin:0;font-size:12.2px;font-weight:700;}
  .info p{margin:0 0 10px;}
  .info-left{left:36px;}
  .info-right{left:770px;}
  .centre{position:absolute;left:300px;width:500px;top:28px;text-align:center;}
  .centre .brand{font-weight:700;font-size:30px;color:var(--white);margin:0;}
  .centre .title{font-family:"Courgette",cursive;font-size:50px;color:var(--berry);margin:10px 0 0;line-height:64px;font-weight:400;}
  .centre .kind{font-family:"Roboto",sans-serif;font-weight:500;font-size:17px;letter-spacing:1px;color:var(--berry);margin:6px 0 0;}
  .skin{position:absolute;left:0;right:0;top:222px;text-align:center;font-family:"Roboto",sans-serif;font-weight:500;font-size:13px;letter-spacing:1.5px;margin:0;}
  .size{position:absolute;left:0;right:0;top:278px;text-align:center;font-family:"Roboto",sans-serif;font-weight:500;font-size:12px;margin:0;}
  .badges{position:absolute;top:250px;display:flex;gap:11px;}
  .badges-left{left:36px;}
  .badges-right{right:46px;}
  .badge{width:40px;height:40px;border:1.5px solid var(--ink);border-radius:50%;box-sizing:border-box;}
</style>
</head>
<body>

<svg class="lid-label" viewBox="0 0 400 400" role="img" aria-label="Round lid label with light sparkle pattern">
  <defs>
    <path id="arc-top" d="M 55,200 A145 145 0 0 1 345,200"/>
    <path id="arc-bottom" d="M 35,200 A165 165 0 0 0 365,200"/>
  </defs>
  <circle cx="200" cy="200" r="195" fill="var(--lid-pink)"/>
  <text class="arc-text"><textPath href="#arc-top" startOffset="50%" text-anchor="middle">WHIPPED BODY SUGAR SCRUB</textPath></text>
  <text class="arc-text"><textPath href="#arc-bottom" startOffset="50%" text-anchor="middle">IDEAL FOR ALL SKIN TYPES</textPath></text>
  <text class="brand" x="200" y="148" text-anchor="middle">Sugarfen &amp; Co</text>
  <text class="title" x="200" y="218" text-anchor="middle">Lumi Dawn</text>
  <text class="title" x="200" y="272" text-anchor="middle">Halo</text>
</svg>

<section class="wrap-label">
  <svg class="field" viewBox="0 0 1100 314" preserveAspectRatio="none" role="img" aria-label="Pink label field with light sparkle pattern and white lower band">
    <rect width="1100" height="314" fill="var(--label-pink)"/>
    <path d="M0,232 Q550,190 1100,232 L1100,314 L0,314 Z" fill="var(--band)"/>
  </svg>

  <div class="info info-left">
    <h3>Ingredients:</h3>
    <p>Pure Cane Sugar, Extra Virgin Coconut Oil, Mango Butter, Kukum Butter, Emulsifying Wax, Jojoba Seed Oil, Sweet Almond Oil, Strawberry Essential Oil, and Pomegranate Essential Oil.</p>
    <h3>Storage/Shelf Life of Product:</h3>
    <p>For best results, stir/mix scrub with the wooden or plastic spoon before each use. The shelf life of all sugar scrubs is 6-8 weeks. Keep the product in a cool, dry place, away from hot or heated temperatures.</p>
  </div>

  <div class="centre">
    <p class="brand">Sugarfen &amp; Co</p>
    <h1 class="title">Lumi Dawn Halo</h1>
    <p class="kind">WHIPPED BODY SUGAR SCRUB</p>
  </div>

  <div class="info info-right">
    <h3>Directions to use Body Sugar Scrub:</h3>
    <p>Apply to wet skin gently in a circular motion on desired body area, hands, feet, legs, arms, etc. Once you have a good scrub, rinse, pat dry, and enjoy soft, hydrated skin. Best to use in the shower. Use between 2-3 times a week if needed.</p>
    <h3>*Cautions:</h3>
    <p>(1) Allergy: Approach this product with extreme caution, if you have allergies<br>(2) Avoid direct contact with eyes</p>
  </div>

  <p class="skin">IDEAL FOR ALL SKIN TYPES</p>
  <p class="size">8oz</p>

  <div class="badges badges-left"><span class="badge"></span><span class="badge"></span><span class="badge"></span></div>
  <div class="badges badges-right"><span class="badge"></span><span class="badge"></span><span class="badge"></span></div>
</section>

</body>
</html>
```